Business Card Design Project - Industrial Motor Rep

Create a business card that utilizes our existing logo found on our website: www.brivanequipco.com

We are a Industrial Distributor with a focus on electric motors. We represent several key brands which can be found on our web site. Our customer base includes Consultants, Large End Users (VX, Harl Chemical, Telvo) and original equipment manufacturers.

Industry/Entity Type

Business

Requirements
Must have
• Name, Title, Phone, Fax, Cell, Website, Mailing address

```html
<!DOCTYPE html>
<html lang="en">
<head>
<meta charset="utf-8">
<title>Brivan Equipco Sales – Business Card</title>
<link href="https://fonts.googleapis.com/css2?family=Inconsolata:wght@400;600&display=swap" rel="stylesheet">
<style>
  :root {
    --backdrop: #e9e7e4;
    --card-red: #d80000;
    --card-red-deep: #b80000;
    --strip-light: #e4e4e4;
    --strip-dark: #a9a9a9;
    --pill-bg: #f6f6f6;
    --ink-red: #d40000;
    --ink-white: #ffffff;
    --badge-grey: #8d96a3;
  }
  * { margin: 0; padding: 0; box-sizing: border-box; }
  html, body {
    width: 1200px; height: 888px; overflow: hidden;
    background: var(--backdrop);
    font-family: "Inconsolata", monospace;
  }
  .canvas { position: relative; width: 1200px; height: 888px; }

  .card {
    position: absolute;
    left: 340px;
    width: 540px;
    border-radius: 24px;
    overflow: hidden;
    background: linear-gradient(135deg, var(--card-red) 0%, var(--card-red) 60%, var(--card-red-deep) 100%);
    box-shadow: 0 6px 14px rgba(0,0,0,0.35);
  }
  .card--front { top: 136px; height: 304px; }
  .card--back  { top: 484px; height: 296px; }

  .side-strip {
    position: absolute; left: 0; top: 0; bottom: 0; width: 70px;
    background: linear-gradient(90deg, var(--strip-light) 0%, #d2d2d2 55%, var(--strip-dark) 100%);
  }
  .brand-badge {
    position: absolute; left: 40px; top: 40px; width: 72px; height: 72px;
    border-radius: 50%;
    background: radial-gradient(circle at 40% 35%, #c7ccd3, var(--badge-grey));
    border: 4px solid #f0f0f0;
  }
  .brand-pill {
    position: absolute; left: 140px; top: 48px; width: 356px; height: 58px;
    border-radius: 29px;
    background: var(--pill-bg);
    display: flex; align-items: center; justify-content: center;
    color: var(--ink-red);
    font-size: 26px; font-weight: 400; letter-spacing: 0.5px;
  }
  .contact {
    position: absolute; left: 184px; top: 124px;
    color: var(--ink-white);
  }
  .contact__name, .contact__title { font-size: 21px; line-height: 25px; }
  .contact__lines { margin-top: 10px; list-style: none; font-size: 12.5px; line-height: 15px; }

  .back-name {
    position: absolute; left: 0; right: 0; top: 58px;
    text-align: center;
    color: var(--ink-white);
    font-size: 36px; font-weight: 600; letter-spacing: 1px;
  }
</style>
</head>
<body>
<main class="canvas">
  <section class="card card--front" aria-label="Business card front">
    <div class="side-strip"></div>
    <div class="brand-badge" aria-hidden="true"></div>
    <div class="brand-pill">Brivan Equipco Sales</div>
    <div class="contact">
      <p class="contact__name">John Smith</p>
      <p class="contact__title">Special Job Title</p>
      <ul class="contact__lines">
        <li>land line: 01632 960000</li>
        <li>mobile: 07700900000</li>
        <li>fax: 01632 960001</li>
        <li>Sales@BrivanEquipco.com</li>
        <li>www.brivanequipco.com</li>
      </ul>
    </div>
  </section>

  <section class="card card--back" aria-label="Business card back">
    <p class="back-name">Brivan Equipco Sales</p>
  </section>
</main>
</body>
</html>
```